CODED website - Breakfree418

I am a successful entrepreneur - have recently sold my business and am semi-retired. I want to give something back, as well as provide a blog for articles and my journeys.

I will also be using this to provide free business and entrepreneurial advice.

I am creating a NOT FOR PROFIT business called Breakfree418.com.au which will provide the following;

1. Blog and articles; my travels, Small to Medium business advice and articles

2. My Bucket List - the 100 things I aim to achieve

3. Free business / start up advice - a section on the website which provides case studies on people / businesses which ask me for advice. We will then chronicle their story and what advice we have given for them to succeed.

My inspiration is the Martin Okonkwo idea and website;

http://martinokonkwo.example/about-martin/

Obviously I do NOT want a copy of this site, but use this for inspiration.

Furthermore, I would be interested in ongoing collaboration with the successful designer - I will be providing advice and consultancy to start ups, all of which will need web design etc, so there is ongoing referral streams for the successful designer.

I need this to be CODED and then uplifted to the website, so please DO NOT bid on this unless you can provide a coded site and facilitate the upload to WildHostings.

The NECESSARY tabs / pages

Main landing page - a short introduction into the ethos of Breakfree418

Writing - this will be the blog articles

About

Our Bucket List - a section where we can add our 100 buket list items. Hyperlinked to open a new page which has details on each bucket list item (ie #1 Make Breakfree418 - hyperlink to a new page which then has info on the bucklist item and what we have done)

Breakfree418 - this will be the section where we discuss people / businesses that we are helping. We will have an opening intro section + a link to the contact us page so they can ask us for the free advice. This will be the section where we have case studies into businesses / people that we have helped.
Updates

Hey everyone!

I'm really keen to get this website launched and looking amazing - if you have any questions, or would like to discuss anything at all, please email me at

dave@pinnaclepost.example.au

As I mentioned in the brief, I am doing this site to give back; I will not be earning a cent, and I will not be trying to earn any funds. I'm doing it simply to help other start ups or entrepreneurs, so I really want this site to look amazing.

I hope someone reads this and is inspired, and wants to be involved in this social enterprise with me.

Really excited to hear from you all and see your designs!

Industry/Entity Type

Business

Requirements
Must have
• MUST BE CODED and uplifted to the WildHosting registered domain - www.breakfree418.com.au - happy to discuss additional costings for this with successful designer.

Separate pages for each section (as outlined in the brief above)

Blog section to look similar to http://martinokonkwo.example/3x5/

Comprehensive website - not a simple wordpress template theme with some minor modifications. I will immediately reject any simple template design. I am looking for a slick, fully functioning website design.

PLEASE BE AWARE that I am looking for ongoing collaboration with the www.breakfree418.com.au.

I am trying this website as I want to find a young, energetic, vibrant, dynamic designer - this is your opportunity to be a part of something big, as this website will be huge!

Please do not submit a design if you are not motivated and ready for something big.

```html
<!DOCTYPE html>
<html lang="en">
<head>
<meta charset="utf-8">
<title>About Breakfree418</title>
<link href="https://fonts.googleapis.com/css2?family=Oswald:wght@300;400&family=Tinos:ital,wght@0,400;0,700;1,400&display=swap" rel="stylesheet">
<style>
  :root {
    --page: #f1f1ef;
    --ink: #3a3a3a;
    --ink-soft: #555;
    --teal: #8fadab;
    --sand: #dccf9a;
    --rust: #d3643e;
    --footer: #262626;
    --footer-text: #bdbdbd;
    --white: #ffffff;
    --rule: #8a8a8a;
  }
  * { box-sizing: border-box; margin: 0; padding: 0; }
  html, body { width: 891px; height: 1200px; overflow: hidden; background: var(--page); }
  body { position: relative; font-family: "Tinos", "Times New Roman", serif; color: var(--ink); }

  /* Header */
  .site-header { position: absolute; left: 0; top: 0; width: 891px; height: 75px; background: var(--page); }
  .brand { position: absolute; left: 142px; top: 22px; font-family: "Oswald", sans-serif; font-weight: 400; font-size: 24px; letter-spacing: 1px; color: #4a4a4a; line-height: 1; }
  .main-nav { position: absolute; left: 312px; top: 21px; display: flex; }
  .main-nav a { font-family: "Oswald", sans-serif; font-weight: 300; font-size: 15px; color: #333; text-decoration: none; padding: 3px 8px; margin-right: 7px; line-height: 21px; }
  .main-nav a.is-current { background: var(--teal); color: var(--white); }

  /* Title band */
  .title-band { position: absolute; left: 0; top: 75px; width: 891px; height: 93px; background: var(--teal); }
  .title-band h1 { position: absolute; left: 180px; top: 20px; font-family: "Oswald", sans-serif; font-weight: 300; font-size: 32px; color: var(--white); letter-spacing: 0.5px; }
  .double-rule { position: absolute; height: 5px; border-top: 1px solid rgba(255,255,255,.6); border-bottom: 1px solid rgba(255,255,255,.6); }

  /* Intro */
  .intro { position: absolute; top: 210px; left: 135px; width: 618px; display: flex; gap: 18px; font-size: 11px; line-height: 15.5px; color: var(--ink); }
  .intro .col { width: 300px; }
  .intro p + p { margin-top: 13px; }

  /* Process */
  .process { position: absolute; left: 0; top: 435px; width: 891px; height: 233px; background: var(--sand); }
  .section-label { position: absolute; font-family: "Oswald", sans-serif; font-weight: 300; font-size: 14px; color: #333; letter-spacing: .3px; }
  .hair { position: absolute; height: 1px; background: var(--rule); }
  .process .hair { background: rgba(255,255,255,.8); }
  .step { position: absolute; top: 40px; width: 150px; text-align: center; }
  .step-art { width: 144px; height: 144px; border-radius: 50%; margin: 0 auto; background: radial-gradient(circle, #3a3631 0 22%, #e4d9ab 23% 100%); border: 1px solid rgba(255,255,255,.7); }
  .step-name { font-family: "Oswald", sans-serif; font-weight: 300; font-size: 21px; color: var(--rust); margin-top: 16px; }

  /* People */
  .card { position: absolute; background: var(--white); box-shadow: 0 2px 4px rgba(0,0,0,.18); }
  .profile { left: 135px; top: 732px; width: 303px; height: 225px; }
  .portrait { position: absolute; left: 18px; top: 12px; width: 122px; height: 122px; border-radius: 50%; background: radial-gradient(circle at 50% 40%, #d9d9d9, #8c8c8c); border: 3px solid #e5e5e5; }
  .card h2 { font-family: "Oswald", sans-serif; font-weight: 300; font-size: 21px; color: #2b2b2b; line-height: 1.05; }
  .profile h2 { position: absolute; left: 156px; top: 18px; }
  .role { font-style: italic; font-size: 9px; color: #333; }
  .handle { font-size: 9px; color: var(--rust); }
  .profile .meta { position: absolute; left: 156px; top: 47px; line-height: 13px; }
  .profile .bio { position: absolute; left: 10px; top: 136px; width: 283px; font-size: 9.5px; line-height: 14px; color: var(--ink-soft); }
  .book { left: 453px; top: 732px; width: 302px; height: 164px; padding: 20px 8px 0; }
  .book .meta { margin-top: 7px; line-height: 13px; }
  .book .blurb { margin-top: 4px; font-size: 9.5px; line-height: 14px; color: var(--ink-soft); }

  .back-to-top { position: absolute; right: 144px; top: 1000px; display: flex; align-items: center; gap: 5px; font-family: "Oswald", sans-serif; font-weight: 300; font-size: 14px; color: var(--rust); text-decoration: none; }

  /* Footer */
  .site-footer { position: absolute; left: 0; top: 1028px; width: 891px; height: 172px; background: var(--footer); color: var(--footer-text); font-size: 10px; line-height: 15px; }
  .foot-col { position: absolute; top: 20px; text-align: center; }
  .foot-col h3 { font-family: "Oswald", sans-serif; font-weight: 300; font-size: 15px; color: var(--white); margin-bottom: 8px; }
  .foot-col .hl { color: var(--rust); }
  .contact { left: 132px; width: 150px; }
  .follow { left: 310px; width: 120px; text-align: left; }
  .follow h3 { text-align: center; }
  .follow li { list-style: none; display: flex; align-items: center; gap: 6px; color: var(--rust); margin-bottom: 3px; }
  .follow li span.dot { width: 10px; height: 10px; background: #8a8a8a; border-radius: 2px; }
  .mailing { left: 447px; width: 150px; }
  .email-field { display: block; width: 134px; height: 20px; margin: 8px auto 0; border: 0; padding: 0 8px; font-family: "Tinos", serif; font-style: italic; font-size: 10px; color: #555; background: var(--white); }
  .subscribe { display: block; width: 88px; height: 30px; margin: 8px auto 0; border: 0; background: var(--rust); color: var(--white); font-family: "Oswald", sans-serif; font-weight: 300; font-size: 14px; }
  .foot-brand { left: 628px; top: 18px; width: 120px; }
  .foot-brand .brand-name { font-family: "Oswald", sans-serif; font-weight: 400; font-size: 19px; letter-spacing: 1px; color: #cfcfcf; line-height: 1; }
  .foot-brand .copy { margin-top: 10px; }
</style>
</head>
<body>

<header class="site-header">
  <div class="brand">BREAKFREE418</div>
  <nav class="main-nav">
    <a href="#" class="is-current">HOME</a>
    <a href="#">ABOUT</a>
    <a href="#">BUCKET LIST</a>
    <a href="#">BREAKFREE418</a>
    <a href="#">WRITING</a>
    <a href="#">CONTACT</a>
  </nav>
</header>

<section class="title-band">
  <div class="double-rule" style="left:135px;top:42px;width:35px"></div>
  <h1>ABOUT BREAKFREE418</h1>
  <div class="double-rule" style="left:510px;top:42px;width:243px"></div>
</section>

<section class="intro">
  <div class="col">
    <p>Phasellus sit amet massa et sapien fringilla interdum. Nullam tincidunt blandit volutpat. In hac habitasse platea dictumst. Mauris et libero eget ante blandit pharetra vitae sit amet neque. Praesent consequat justo vitae purus feugiat hendrerit. Pellentesque euismod semper arcu in commodo. Sed iaculis iaculis mollis. Etiam cursus ultrices pulvinar.</p>
    <p>Class aptent taciti sociosqu ad litora torquent per conubia nostra, per inceptos himenaeos. Pellentesque hendrerit commodo urna sed bibendum. Sed a enim vel ligula condimentum varius gravida ac eros. Suspendisse potenti. Cras molestie, velit vel facilisis lacinia, odio dui mattis massa, at imperdiet justo ligula sit amet mi. Quisque cursus, eros vitae pulvinar blandit, velit sapien tincidunt erat.</p>
  </div>
  <div class="col">
    <p>Etiam congue consequat diam sit amet faucibus. Integer nunc velit, pretium a dapibus et, fermentum vitae ante. Donec aliquam mi sed odio congue vel tempus nisl bibendum. Vivamus commodo, nisi at fermentum placerat, velit nisl volutpat lacus, ac laoreet mauris tortor vitae eros. Sed pellentesque lorem nibh. Fusce dignissim sapien et tortor pulvinar vitae dictum urna elementum. Lorem ipsum dolor sit amet, consectetur adipiscing elit. Cras mattis pharetra varius. Ut pharetra, nibh sit amet bibendum ornare, mauris enim interdum leo, nec molestie arcu metus sed est. Maecenas elit eros, pretium eu tempus id, feugiat vitae metus. Suspendisse placerat nibh eget sapien dignissim at vestibulum lacus vehicula.</p>
  </div>
</section>

<section class="process">
  <div class="hair" style="left:135px;top:20px;width:33px"></div>
  <span class="section-label" style="left:175px;top:10px">OUR PROCESS</span>
  <div class="hair" style="left:260px;top:20px;width:493px"></div>
  <div class="step" style="left:135px">
    <div class="step-art" role="img" aria-label="Blueprint sketch of a rocket"></div>
    <div class="step-name">PLAN</div>
  </div>
  <div class="step" style="left:292px">
    <div class="step-art" role="img" aria-label="Striped rocket under construction"></div>
    <div class="step-name">DESIGN</div>
  </div>
  <div class="step" style="left:450px">
    <div class="step-art" role="img" aria-label="Rocket with gears inside"></div>
    <div class="step-name">ACT</div>
  </div>
  <div class="step" style="left:607px">
    <div class="step-art" role="img" aria-label="Finished rocket launching"></div>
    <div class="step-name">IMPROVE</div>
  </div>
</section>

<div class="hair" style="left:135px;top:708px;width:33px"></div>
<span class="section-label" style="left:175px;top:698px">WHO IS BEHIND BREAKFREE418?</span>
<div class="hair" style="left:360px;top:708px;width:393px"></div>

<article class="card profile">
  <div class="portrait" role="img" aria-label="Portrait photo of Dave"></div>
  <h2>DAVE</h2>
  <div class="meta">
    <div class="role">Serial Entrepreneur</div>
    <div class="handle">@breakfree418</div>
  </div>
  <p class="bio">Nullam blandit laoreet risus ut iaculis. Proin in lorem vel ligula auctor consectetur lacinia vitae massa. Mauris dictum egestas leo, non interdum mi egestas quis. Vestibulum volutpat, urna nec lacinia lobortis, mauris leo dictum urna, quis rhoncus est libero non libero. Ut eget leo mauris. Fusce risus orci, fringilla at cursus et, posuere nec metus.</p>
</article>

<article class="card book">
  <h2>MY LATEST<br>BOOK</h2>
  <div class="meta">
    <div class="role">How to be successful in Business</div>
    <div class="handle">@lumenreads</div>
  </div>
  <p class="blurb">Vivamus odio elit, euismod sed consectetur tempus, eleifend a lacus. Etiam eu rutrum dui. Suspendisse a lectus quis massa gravida sollicitudin. Morbi sagittis egestas nibh vitae consectetur. Ut lectus ligula, rutrum nec molestie nec, egestas in dui.</p>
</article>

<a href="#" class="back-to-top">BACK TO TOP
  <svg width="20" height="20" viewBox="0 0 20 20" aria-hidden="true"><circle cx="10" cy="10" r="10" fill="#d3643e"/><path d="M5.5 12 L10 7.5 L14.5 12" stroke="#fff" stroke-width="2.4" fill="none" stroke-linecap="round" stroke-linejoin="round"/></svg>
</a>

<footer class="site-footer">
  <div class="foot-col contact">
    <h3>CONTACT</h3>
    <p>Address: <span style="color:#ddd">27 Harbour Lane,<br>Kelso, Scotland, UK</span></p>
    <p>Tel: <span style="color:#ddd">+44 1555-010-482</span></p>
    <p>Email: <span class="hl">hello@breakfree418.com.au</span></p>
  </div>
  <div class="foot-col follow">
    <h3>FOLLOW US</h3>
    <ul>
      <li><span class="dot"></span>Like us on Facefolio</li>
      <li><span class="dot"></span>Follow us on Chirper</li>
      <li><span class="dot" style="border-radius:50%"></span>W.I.P. on Drizzle</li>
    </ul>
  </div>
  <div class="foot-col mailing">
    <h3>MAILING LIST</h3>
    <p>Sign up if you would like to receive updates from BREAKFREE418.</p>
    <input class="email-field" type="text" placeholder="Enter your email address">
    <button class="subscribe" type="button">SUBSCRIBE</button>
  </div>
  <div class="foot-col foot-brand">
    <div class="brand-name">BREAKFREE418</div>
    <p class="copy">© 2012 BREAKFREE418</p>
  </div>
</footer>

</body>
</html>
```